Make attractive Packaging label for NUT BUTTERS jars

We at Velvet Orchard are launching our own line of NUT BUTTERS. We will be serving them in GLASS JARS ready packaged. I need attractive luxurious design for glass jar and should be designed ready to print.
I have attached glass jar pictures and measurement sheet.
My company logo has been attached. Also company details can be found on our facebook page.
product will be

ALMOND BUTTER
CASHEW BUTTER
PEANUT BUTTER
HAZELNUT BUTTER.

```html
<!DOCTYPE html>
<html lang="en">
<head>
<meta charset="utf-8">
<title>Velvet Orchard – Nut Butter Labels</title>
<link href="https://fonts.googleapis.com/css2?family=Open+Sans:wght@600;700;800&family=Lobster+Two:wght@700&display=swap" rel="stylesheet">
<style>
  :root{
    --almond:#f5891f;
    --cashew:#a6e23a;
    --peanut:#d3302a;
    --hazelnut:#fcc21a;
    --brand-brown:#8a5424;
    --choc:#3b2113;
    --cream:#f7f0e3;
    --ink:#111111;
    --lid-grey:#c9c9c9;
    --panel-top:#dd7418;
    --panel-bottom:#fbd2a9;
    --col-almond:#fbb877;
    --col-cashew:#eef69c;
    --col-peanut:#f36fa6;
    --col-hazelnut:#fcd944;
    --nut-almond:#b57443;
    --nut-cashew:#e0b57a;
    --nut-peanut:#c79a64;
    --nut-hazelnut:#8f5a2b;
  }
  *{box-sizing:border-box;margin:0;padding:0}
  html,body{width:1200px;height:1000px;overflow:hidden;background:#fff}
  body{font-family:"Open Sans",Arial,sans-serif;position:relative}

  .board{position:relative;width:1200px;height:1000px;background:#fff}

  /* ---------- round label (seal) ---------- */
  .seal{position:absolute;width:10em;height:10em;border-radius:50%;
        background:var(--cream);border:.62em solid var(--tone);overflow:hidden}
  .seal__brand{position:absolute;left:0;right:0;top:14%;text-align:center;
        font-weight:800;color:var(--brand-brown);font-size:1.45em;line-height:1.05}
  .seal__band{position:absolute;left:0;right:0;top:49%;height:12%;background:var(--tone);
        display:flex;align-items:center;justify-content:center;
        font-weight:600;font-size:.68em;letter-spacing:.02em;color:var(--ink)}
  .seal__nuts{position:absolute;left:37%;top:67%;width:26%;height:15%;border-radius:50%;
        background:radial-gradient(ellipse at 40% 40%,var(--nut-light),var(--nut))}

  .tone-almond{--tone:var(--almond);--nut:var(--nut-almond);--nut-light:#d9a073}
  .tone-cashew{--tone:var(--cashew);--nut:var(--nut-cashew);--nut-light:#f3d9ac}
  .tone-peanut{--tone:var(--peanut);--nut:var(--nut-peanut);--nut-light:#e6c699}
  .tone-hazelnut{--tone:var(--hazelnut);--nut:var(--nut-hazelnut);--nut-light:#c08a55}

  .seal--side{font-size:21px;left:38px}
  .seal--peanut-band .seal__band,.seal--dark-band .seal__band{color:#fff}

  /* ---------- top panel ---------- */
  .showcase{position:absolute;left:310px;top:0;width:890px;height:500px;
        background:linear-gradient(180deg,var(--panel-top) 0%,#f3a766 22%,var(--panel-bottom) 55%,var(--panel-bottom) 100%)}
  .showcase__note{position:absolute;left:16px;top:12px;font-size:13px;color:var(--ink)}
  .showcase__brand{position:absolute;left:0;right:0;top:58px;text-align:center;
        font-weight:800;color:var(--brand-brown);font-size:72px;line-height:1.02}

  /* ---------- flat front label ---------- */
  .front{position:absolute;width:170px;height:118px;background:var(--cream);overflow:hidden;border-radius:4px}
  .front__brand{position:absolute;left:10px;top:10px;font-weight:800;color:var(--brand-brown);
        font-size:21px;line-height:1.05}
  .front__band{position:absolute;left:0;right:0;bottom:0;height:46px;background:var(--tone)}
  .front__flavour{position:absolute;right:6px;bottom:6px;width:96px;height:58px;
        background:var(--choc);border-radius:48% 40% 44% 52%/55% 45% 50% 45%;
        color:#fff;text-align:center;padding-top:6px}
  .front__name{font-family:"Lobster Two",Georgia,serif;font-weight:700;font-size:21px;line-height:1}
  .front__kind{font-size:10px;font-weight:600;letter-spacing:.05em;margin-top:2px}

  /* ---------- lower columns ---------- */
  .variants{position:absolute;left:310px;top:503px;width:890px;height:497px;display:flex}
  .variant{position:relative;flex:1}
  .variant--almond{background:var(--col-almond)}
  .variant--cashew{background:var(--col-cashew)}
  .variant--peanut{background:var(--col-peanut)}
  .variant--hazelnut{background:var(--col-hazelnut)}
  .variants__heading{position:absolute;left:310px;width:890px;text-align:center;
        font-weight:800;font-size:27px;color:var(--ink);letter-spacing:.01em}
  .variants__heading--lid{top:520px}
  .variants__heading--front{top:735px}

  .lid{position:absolute;left:50%;top:60px;width:172px;height:172px;margin-left:-86px;border-radius:50%;
       background:radial-gradient(circle,#fafafa 60%,var(--lid-grey) 78%,#f2f2f2 92%,#a9a9a9 100%);
       box-shadow:0 2px 4px rgba(0,0,0,.25)}
  .seal--lid{font-size:15px;left:11px;top:11px}
  .variant .front{left:50%;margin-left:-85px;top:320px}
</style>
</head>
<body>
<main class="board">

  <!-- side column: flat round labels -->
  <div class="seal seal--side tone-almond" style="top:15px">
    <div class="seal__brand">Velvet<br>Orchard</div>
    <div class="seal__band">ALMOND BUTTER</div>
    <div class="seal__nuts" role="img" aria-label="Photo of almonds with a leaf"></div>
  </div>
  <div class="seal seal--side tone-cashew" style="top:265px">
    <div class="seal__brand">Velvet<br>Orchard</div>
    <div class="seal__band">CASHEW BUTTER</div>
    <div class="seal__nuts" role="img" aria-label="Photo of cashews with a leaf"></div>
  </div>
  <div class="seal seal--side seal--dark-band tone-peanut" style="top:515px">
    <div class="seal__brand">Velvet<br>Orchard</div>
    <div class="seal__band">PEANUT BUTTER</div>
    <div class="seal__nuts" role="img" aria-label="Photo of peanuts in and out of the shell"></div>
  </div>
  <div class="seal seal--side tone-hazelnut" style="top:765px">
    <div class="seal__brand">Velvet<br>Orchard</div>
    <div class="seal__band">HAZELNUT BUTTER</div>
    <div class="seal__nuts" role="img" aria-label="Photo of hazelnuts with a leaf"></div>
  </div>

  <!-- top panel: brand and range -->
  <section class="showcase">
    <p class="showcase__note">*For presentation purpose only.</p>
    <h1 class="showcase__brand">Velvet<br>Orchard</h1>

    <div class="front tone-almond" style="left:95px;top:310px">
      <div class="front__brand">Velvet<br>Orchard</div>
      <div class="front__band"></div>
      <div class="front__flavour"><div class="front__name">Almond</div><div class="front__kind">BUTTER</div></div>
    </div>
    <div class="front tone-cashew" style="left:275px;top:310px">
      <div class="front__brand">Velvet<br>Orchard</div>
      <div class="front__band"></div>
      <div class="front__flavour"><div class="front__name">Cashew</div><div class="front__kind">BUTTER</div></div>
    </div>
    <div class="front tone-peanut" style="left:455px;top:310px">
      <div class="front__brand">Velvet<br>Orchard</div>
      <div class="front__band"></div>
      <div class="front__flavour"><div class="front__name">Peanut</div><div class="front__kind">BUTTER</div></div>
    </div>
    <div class="front tone-hazelnut" style="left:635px;top:310px">
      <div class="front__brand">Velvet<br>Orchard</div>
      <div class="front__band"></div>
      <div class="front__flavour"><div class="front__name">Hazelnut</div><div class="front__kind">BUTTER</div></div>
    </div>
  </section>

  <!-- lower panel: lid and front per flavour -->
  <section class="variants">
    <div class="variant variant--almond">
      <div class="lid">
        <div class="seal seal--lid tone-almond">
          <div class="seal__brand">Velvet<br>Orchard</div>
          <div class="seal__band">ALMOND BUTTER</div>
          <div class="seal__nuts" role="img" aria-label="Photo of almonds"></div>
        </div>
      </div>
      <div class="front tone-almond">
        <div class="front__brand">Velvet<br>Orchard</div>
        <div class="front__band"></div>
        <div class="front__flavour"><div class="front__name">Almond</div><div class="front__kind">BUTTER</div></div>
      </div>
    </div>
    <div class="variant variant--cashew">
      <div class="lid">
        <div class="seal seal--lid tone-cashew">
          <div class="seal__brand">Velvet<br>Orchard</div>
          <div class="seal__band">CASHEW BUTTER</div>
          <div class="seal__nuts" role="img" aria-label="Photo of cashews"></div>
        </div>
      </div>
      <div class="front tone-cashew">
        <div class="front__brand">Velvet<br>Orchard</div>
        <div class="front__band"></div>
        <div class="front__flavour"><div class="front__name">Cashew</div><div class="front__kind">BUTTER</div></div>
      </div>
    </div>
    <div class="variant variant--peanut">
      <div class="lid">
        <div class="seal seal--lid seal--dark-band tone-peanut">
          <div class="seal__brand">Velvet<br>Orchard</div>
          <div class="seal__band">PEANUT BUTTER</div>
          <div class="seal__nuts" role="img" aria-label="Photo of peanuts"></div>
        </div>
      </div>
      <div class="front tone-peanut">
        <div class="front__brand">Velvet<br>Orchard</div>
        <div class="front__band"></div>
        <div class="front__flavour"><div class="front__name">Peanut</div><div class="front__kind">BUTTER</div></div>
      </div>
    </div>
    <div class="variant variant--hazelnut">
      <div class="lid">
        <div class="seal seal--lid tone-hazelnut">
          <div class="seal__brand">Velvet<br>Orchard</div>
          <div class="seal__band">HAZELNUT BUTTER</div>
          <div class="seal__nuts" role="img" aria-label="Photo of hazelnuts"></div>
        </div>
      </div>
      <div class="front tone-hazelnut">
        <div class="front__brand">Velvet<br>Orchard</div>
        <div class="front__band"></div>
        <div class="front__flavour"><div class="front__name">Hazelnut</div><div class="front__kind">BUTTER</div></div>
      </div>
    </div>
  </section>
  <h2 class="variants__heading variants__heading--lid">TOP LID</h2>
  <h2 class="variants__heading variants__heading--front">FRONT</h2>

</main>
</body>
</html>
```